User help guide for software for investment bank

We need a professional design for our user help guides for new software we have written for our client. We develop visualization software for investment banks in Singapore mainly focused in the financial and risk management area. Our help guides are design to show them how the software works as well as promote our brand
Updates

Project Deadline Extended Reason: I am looking for more alternative designs and we have around 10 more documents to do after this Added Saturday, November 21, 2015

Target Market(s)

Investment banking, risk management, finance

Industry/Entity Type

Bank

Requirements
Must have
• Content of document and logos
• Colour sheme
• Professional brouchure design
• Quorvin and bimsot logos on it
• Look at www.quorvin-example.com for company looks and feel
• PLEASE USE COLOUR SCHEMES BELOW IN ATTACHMENT AND FOLLOW SIMILAR STYLE TO CLIENT ANNUAL REPORT

```html
<!DOCTYPE html>
<html lang="en">
<head>
<meta charset="utf-8">
<title>User Guide – Web Editor Tool</title>
<link rel="stylesheet" href="https://fonts.googleapis.com/css2?family=Open+Sans:wght@300;400;600&display=swap">
<style>
  :root {
    --brand-blue: #1c4279;
    --paper: #ffffff;
    --ink: #58595b;
    --ink-strong: #4d4d4f;
    --table-head: #58585a;
    --row-light: #dcdcdc;
    --row-dark: #a7a7a8;
    --row-text: #ffffff;
  }
  * { margin: 0; padding: 0; box-sizing: border-box; }
  html, body { width: 849px; height: 1200px; overflow: hidden; background: var(--paper); }
  .page {
    position: relative; width: 849px; height: 1200px;
    font-family: "Open Sans", Arial, sans-serif; color: var(--ink);
    font-weight: 300; font-size: 17px; line-height: 18.8px;
  }
  .sidebar {
    position: absolute; left: 0; top: 0; width: 212px; height: 1200px;
    background: var(--brand-blue);
  }
  .page-number {
    position: absolute; left: 55px; top: 1118px;
    color: var(--paper); font-size: 25px; font-weight: 300;
  }
  .block { position: absolute; left: 269px; width: 540px; white-space: nowrap; }
  .section-title { font-weight: 600; font-size: 17.5px; color: var(--ink-strong); line-height: 22px; }
  .bullets { list-style: none; }
  .bullets > li { position: relative; padding-left: 21px; }
  .bullets > li::before {
    content: ""; position: absolute; left: 2px; top: 5px;
    width: 9px; height: 9px; background: var(--ink);
  }
  .sub { display: block; padding-left: 1px; }
  .roles-table {
    position: absolute; left: 269px; top: 336px; width: 523px;
    border-collapse: collapse; font-size: 14.5px; line-height: 16px;
  }
  .roles-table th {
    background: var(--table-head); color: var(--row-text); font-weight: 300;
    height: 86px; text-align: left; padding: 0 14px; vertical-align: middle;
    border-right: 1px solid #6a6a6c;
  }
  .roles-table th:last-child { border-right: 0; }
  .roles-table th.center { padding-left: 15px; }
  .roles-table td {
    color: var(--row-text); height: 21.5px; text-align: center; font-size: 14px;
    border-right: 1px solid rgba(255,255,255,0.5); font-weight: 300;
    border-top: 1px solid #ffffff;
  }
  .roles-table td:first-child { text-align: left; padding-left: 14px; }
  .roles-table td:last-child { border-right: 0; }
  .row-light td { background: var(--row-light); }
  .row-dark td { background: var(--row-dark); }
</style>
</head>
<body>
<div class="page">
  <div class="sidebar"></div>
  <div class="page-number">3</div>

  <h2 class="block section-title" style="top:53px">1. User Roles and Permissions</h2>
  <p class="block" style="top:92px">The Web Editor Tool is allowed to be used to all the users that have<br>edit permissions in their user role.</p>

  <div class="block" style="top:149px">
    <p>Currently, RVMT tool has the roles below:</p>
    <ul class="bullets">
      <li>Risk Administrator:<span class="sub">- Can do everything into Quorvin model.</span></li>
      <li>Risk Project Leader
        <span class="sub">- He can modify the report but NOT saving it or create a new one.</span>
        <span class="sub">- He cannot move or delete the current reports stored at server</span>
        <span class="sub">- He cannot set permissions</span></li>
      <li>Risk Publisher<span class="sub">- He can see the reports but do nothing more.</span></li>
    </ul>
  </div>

  <table class="roles-table">
    <colgroup><col style="width:169px"><col style="width:118px"><col style="width:118px"><col style="width:118px"></colgroup>
    <thead>
      <tr>
        <th>USER NAME</th>
        <th class="center">Can access to<br>Web Edit Tool</th>
        <th class="center">Can modify<br>the current<br>report but no<br>saving this</th>
        <th class="center">Can create<br>new reports<br>or modify the<br>current ones</th>
      </tr>
    </thead>
    <tbody>
      <tr class="row-light"><td>RISK ADMINISTRATOR</td><td>YES</td><td>N/A</td><td>YES</td></tr>
      <tr class="row-dark"><td>RISK PROJECT LEADER</td><td>YES</td><td>YES</td><td>NO</td></tr>
      <tr class="row-light"><td>RISK PUBLISHER</td><td>NO</td><td>NO</td><td>NO</td></tr>
    </tbody>
  </table>

  <h2 class="block section-title" style="top:523px">2. Restrictions using Web Editor Tool</h2>
  <p class="block" style="top:562px">Web Editor Tool contains big part of the current functionalities<br>included at Quorvin Desktop. This allows to the users to modify or<br>create new reports online, without using Quorvin Desktop. There are<br>some rules that the users must bear in mind using the Web Editor<br>Tool:</p>

  <div class="block" style="top:675px">
    <p>What the Web Editor Tool users can do:</p>
    <ul class="bullets">
      <li>Create new views (sheets), duplicate, and rename views in<br>a workbook</li>
      <li>Change aggregation of measures</li>
      <li>Use Show me to create views</li>
      <li>View underlying data</li>
      <li>Create and edit calculated fields, and use quick table calculations</li>
      <li>Drag field to different mark types in the Marks card</li>
      <li>Use the Analytics pane to drag reference lines, trend lines, and<br>other objects into the view</li>
      <li>Add, modify, and remove filters (Shown as Quick Filters), and edit<br>a filter layout.</li>
      <li>Show labels, totals and subtotals</li>
      <li>Swap X and Y axes</li>
      <li>Change the view size</li>
      <li>Exclude or remove fields in the view</li>
    </ul>
  </div>

  <div class="block" style="top:995px">
    <p>What the Web Editor Tool users cannot do:</p>
    <ul class="bullets">
      <li>Cannot add data sources to a published workbook</li>
      <li>Data model editing is not supported.</li>
      <li>Dashboards and stories cannot be created or modified at<br>the server</li>
      <li>Formatting options are not available</li>
    </ul>
  </div>
</div>
</body>
</html>
```